Funeral Services Web Site

We need a website for a Funeral Services company. The choice of colors is free of charge. One Page Website with 8 sections. Menu: - Home - Our Services - Obituaries -> link to another page. - Our Shop - Funeral Monument - Funeral Contract - Contact Us

Target Market(s)

Every one need Funeral Services

Coding

Coded - Design and coding required

Number of Pages Required

2 page

Font styles to use
Sans Serif
Script

Colors

Designer to choose colors to be used in the design.

```html
<!DOCTYPE html>
<html lang="en">
<head>
<meta charset="utf-8">
<title>Evermore Funeral Home</title>
<link rel="stylesheet" href="https://fonts.googleapis.com/css2?family=Merriweather:wght@400;700&family=Open+Sans:wght@400;600;700&display=swap">
<style>
:root{
  --teal:#00997f;
  --brown:#5b4343;
  --brown-dark:#3d2c2c;
  --text:#555;
  --heading:#333;
  --light:#f4f4f4;
  --serif:'Merriweather',Georgia,serif;
  --sans:'Open Sans',Arial,sans-serif;
}
*{box-sizing:border-box;margin:0;padding:0}
html,body{width:1200px;height:3606px;overflow:hidden}
body{font-family:var(--sans);color:var(--text);position:relative;background:#fff}
.abs{position:absolute}
.btn{position:absolute;background:var(--teal);color:#fff;font-weight:600;font-size:15px;display:flex;align-items:center;justify-content:center;border:0}
.section-title{position:absolute;left:0;width:1200px;text-align:center;font-family:var(--serif);font-weight:700;font-size:24px;color:var(--heading)}

/* top bar & header */
.topbar{left:0;top:0;width:1200px;height:31px;background:var(--brown-dark);color:#fff;font-size:11px}
.topbar .welcome{left:132px;top:8px}
.topbar .info{right:132px;top:8px;display:flex;gap:22px;align-items:center}
.topbar svg{vertical-align:-2px;margin-right:6px}
.header{left:0;top:31px;width:1200px;height:115px;background:var(--brown);box-shadow:0 4px 6px rgba(0,0,0,.3);z-index:2}
.brand{left:132px;top:40px;color:#fff;font-family:var(--serif);font-size:20px;display:flex;align-items:center;gap:8px}
.brand i{width:12px;height:12px;border-radius:50%;background:#fff;display:block}
.nav{right:132px;top:49px;display:flex;gap:26px;color:#fff;font-size:12.5px}

/* hero */
.hero{left:0;top:146px;width:1200px;height:449px;background:linear-gradient(180deg,#2f5f9c 0%,#6d8fb8 30%,#6b4a3f 45%,#3f5a2f 70%,#4f7b2e 100%)}
.hero h1{position:absolute;top:146px;width:1200px;text-align:center;font-family:var(--serif);color:#fff;font-size:40px;letter-spacing:1px;text-shadow:0 2px 4px rgba(0,0,0,.5)}
.hero p{position:absolute;top:200px;width:1200px;text-align:center;color:#fff;font-size:14px}
.dots{position:absolute;display:flex;gap:4px}
.dots i{width:6px;height:6px;border-radius:50%;background:#fff;display:block}
.dots i:first-child{background:var(--teal)}

/* services */
.svc{width:182px;height:147px;background:#fff;box-shadow:0 1px 5px rgba(0,0,0,.18);display:flex;flex-direction:column;align-items:center;justify-content:center;text-align:center;font-size:16px;color:#444;gap:12px;line-height:1.2}

/* obituaries */
.obits{left:0;top:1127px;width:1200px;height:448px;background:var(--light)}
.obit{width:280px}
.obit .photo{position:absolute;left:0;top:0;width:106px;height:102px;background:linear-gradient(135deg,#9a9a9a,#3c3c3c)}
.obit .meta{position:absolute;left:120px;top:8px;font-size:15px;line-height:19px;color:#444}
.obit .meta b.name{font-family:var(--serif);font-size:19px;display:block;margin-bottom:6px;color:#333}
.obit .meta .role{color:#aaa}
.obit .desc{position:absolute;left:0;top:127px;width:280px;font-size:11.5px;line-height:15px}

/* shop */
.product{width:200px;text-align:center}
.product .pic{width:190px;height:196px;margin:0 auto}
.product .name{font-family:var(--serif);font-size:15px;color:#333;margin-top:40px}
.product .price{font-size:20px;color:#333;margin-top:8px}

/* monument */
.monument{left:0;top:2184px;width:1200px;height:399px;background:linear-gradient(90deg,#1b1714 0%,#3a2f27 25%,#23201c 45%,#1c2420 70%,#7d857a 90%,#3e4a40 100%)}
.monument h2{position:absolute;top:72px;width:1200px;text-align:center;font-family:var(--serif);color:#fff;font-size:24px}
.monument .copy{position:absolute;left:231px;top:136px;width:746px;color:#fff;font-size:12px;line-height:15px;text-align:justify}
.monument .copy p{margin-bottom:14px}

/* contact */
.contact h2,.contract h2{font-family:var(--serif);font-size:24px;color:#444}
.lead{font-size:12.5px;line-height:15.5px;text-align:justify}
.info-item{display:flex;gap:18px;width:260px}
.info-item .ic{width:48px;height:48px;border-radius:50%;background:var(--teal);border:3px solid #cfeee8;flex:none;display:flex;align-items:center;justify-content:center}
.info-item h3{font-family:var(--serif);font-size:17px;color:#333;margin:2px 0 8px}
.info-item p{font-size:12.5px;line-height:19px;color:#444}
.form{left:704px;top:2643px;width:363px;height:644px;background:#fff;box-shadow:0 1px 6px rgba(0,0,0,.2);padding:26px 41px}
.form h2{font-family:var(--serif);font-size:24px;color:#444;margin-bottom:18px}
.form label{display:block;font-size:14px;color:#777;margin-bottom:14px}
.form .field{width:281px;height:44px;border:1px solid #e5e5e5;background:#fafafa;margin-bottom:22px}
.form .field.tall{height:113px}

/* footer */
.footer{left:0;top:3340px;width:1200px;height:238px;background:var(--brown);color:#fff}
.footer h3{position:absolute;top:62px;font-family:var(--serif);font-size:19px}
.footer .txt{position:absolute;top:105px;font-size:13px;line-height:15.5px;text-align:justify}
.footer .links{position:absolute;top:105px;display:grid;grid-template-columns:136px 150px;row-gap:9px;font-size:13px}
.bottom{left:0;top:3578px;width:1200px;height:28px;background:var(--brown-dark);color:#fff;font-size:8.5px}
.bottom .legal{left:132px;top:9px;display:flex;gap:20px}
.bottom .social{right:132px;top:7px;display:flex;gap:24px;align-items:center}
.bottom .social i{width:12px;height:12px;border-radius:50%;background:#fff;display:block}
</style>
</head>
<body>

<div class="abs topbar">
  <span class="abs welcome">Welcome to our Funeral Home</span>
  <div class="abs info">
    <span><svg width="9" height="12" viewBox="0 0 9 12"><path d="M4.5 0A4.5 4.5 0 0 0 0 4.5C0 8 4.5 12 4.5 12S9 8 9 4.5A4.5 4.5 0 0 0 4.5 0zm0 6.2a1.7 1.7 0 1 1 0-3.4 1.7 1.7 0 0 1 0 3.4z" fill="#fff"/></svg>View Location</span>
    <span><svg width="11" height="11" viewBox="0 0 24 24"><path d="M6.6 10.8a15 15 0 0 0 6.6 6.6l2.2-2.2c.3-.3.7-.4 1-.2 1.1.4 2.3.6 3.6.6.6 0 1 .4 1 1V20c0 .6-.4 1-1 1A17 17 0 0 1 3 4c0-.6.4-1 1-1h3.5c.6 0 1 .4 1 1 0 1.3.2 2.5.6 3.6.1.3 0 .7-.2 1z" fill="#fff"/></svg>1555-210-734</span>
    <svg width="11" height="11" viewBox="0 0 12 12"><circle cx="5" cy="5" r="3.8" stroke="#fff" stroke-width="1.6" fill="none"/><path d="M8 8l3 3" stroke="#fff" stroke-width="1.8"/></svg>
  </div>
</div>

<header class="abs header">
  <div class="abs brand"><i></i>Evermore</div>
  <nav class="abs nav">
    <span>HOME</span><span>OUR SERVICES</span><span>OBITURIES</span><span>OUR SHOP</span><span>FUNERAL MONUMENT</span><span>FUNERAL CONTRACT</span><span>CONTACT US</span>
  </nav>
</header>

<section class="abs hero" role="img" aria-label="Brick church with a bell tower above a green cemetery with crosses under a blue sky">
  <h1>HELPING YOU COPE WITH GREIF</h1>
  <p>We are here to help you arrange funeral you want for your loved one - Every step of the way</p>
  <span class="btn" style="left:517px;top:244px;width:168px;height:41px">View Our Services</span>
  <div class="dots" style="left:586px;top:389px"><i></i><i></i><i></i></div>
</section>

<h2 class="section-title" style="top:645px">Our Services</h2>
<div class="abs svc" style="left:132px;top:721px">
  <svg width="34" height="40" viewBox="0 0 34 40"><path d="M7 34V12a10 10 0 0 1 20 0v22" fill="none" stroke="#00997f" stroke-width="3"/><path d="M17 10v12M12 15h10M11 26h12M11 30h12" stroke="#00997f" stroke-width="2.4"/><rect x="2" y="34" width="30" height="5" fill="#00997f"/></svg>
  <span>Arranging<br>Funeral</span>
</div>
<div class="abs svc" style="left:381px;top:721px">
  <svg width="40" height="40" viewBox="0 0 40 40"><rect x="9" y="9" width="22" height="22" transform="rotate(45 20 20)" fill="#00997f"/><rect x="14" y="14" width="12" height="12" transform="rotate(45 20 20)" fill="none" stroke="#fff" stroke-width="2"/></svg>
  <span>Memorials</span>
</div>
<div class="abs svc" style="left:636px;top:721px">
  <svg width="48" height="40" viewBox="0 0 48 40"><rect x="12" y="4" width="14" height="22" rx="2" transform="rotate(-40 19 15)" fill="#00997f"/><path d="M22 20l18 14" stroke="#00997f" stroke-width="5"/><rect x="2" y="33" width="22" height="5" fill="#00997f"/></svg>
  <span>Legal Services</span>
</div>
<div class="abs svc" style="left:885px;top:721px">
  <svg width="44" height="40" viewBox="0 0 44 40"><path d="M10 30V6h24v24" fill="none" stroke="#00997f" stroke-width="3.5"/><rect x="4" y="30" width="36" height="6" fill="#00997f"/></svg>
  <span>Burial &amp; Cremation</span>
</div>
<div class="abs svc" style="left:132px;top:924px">
  <svg width="42" height="42" viewBox="0 0 42 42"><circle cx="21" cy="10" r="7" fill="#00997f"/><circle cx="11" cy="19" r="7" fill="#00997f"/><circle cx="31" cy="19" r="7" fill="#00997f"/><path d="M21 16v18M13 36h16" stroke="#00997f" stroke-width="3.5"/></svg>
  <span>Arrangement of<br>Flowers</span>
</div>
<div class="abs svc" style="left:381px;top:924px">
  <svg width="24" height="44" viewBox="0 0 24 44"><path d="M6 2h12l5 12-5 28H6L1 14z" fill="#00997f"/><path d="M12 10v16M7 15h10" stroke="#fff" stroke-width="2.4"/></svg>
  <span>Life Art Coffin</span>
</div>
<div class="abs svc" style="left:636px;top:924px">
  <svg width="62" height="26" viewBox="0 0 62 26"><path d="M2 8h44l10 6h4v8H2z" fill="#00997f"/><rect x="8" y="10" width="5" height="4" fill="#fff"/><rect x="17" y="10" width="5" height="4" fill="#fff"/><rect x="26" y="10" width="5" height="4" fill="#fff"/><rect x="35" y="10" width="5" height="4" fill="#fff"/><circle cx="13" cy="22" r="4" fill="#fff" stroke="#00997f" stroke-width="2.5"/><circle cx="48" cy="22" r="4" fill="#fff" stroke="#00997f" stroke-width="2.5"/></svg>
  <span>Arranging Limousine</span>
</div>
<div class="abs svc" style="left:885px;top:924px">
  <svg width="36" height="42" viewBox="0 0 36 42"><circle cx="18" cy="10" r="8" fill="#00997f"/><path d="M2 42c0-12 6-20 16-20s16 8 16 20z" fill="#00997f"/><path d="M18 26v10M14 30h8" stroke="#fff" stroke-width="2.4"/></svg>
  <span>Arrangement of<br>priest</span>
</div>

<section class="abs obits">
  <h2 class="section-title" style="top:51px">Obituries</h2>
  <div class="abs obit" style="left:132px;top:126px">
    <div class="photo" role="img" aria-label="Black and white portrait photograph"></div>
    <div class="meta"><b class="name">Harold Finch</b><span class="role">Amazing Man</span><br><b>From:</b> 11.08.1937<br><b>To:</b> 14.03.2015</div>
    <p class="desc">Phasellus faucibus ut purus a condimentum. Sed id risus eget sem Phasellus faucibus ut condim tumsodalesm quis.</p>
  </div>
  <div class="abs obit" style="left:459px;top:126px">
    <div class="photo" role="img" aria-label="Black and white portrait photograph"></div>
    <div class="meta"><b class="name">Margaret Lane</b><span class="role">Teacher</span><br><b>From:</b> 11.08.1937<br><b>To:</b> 14.03.2015</div>
    <p class="desc">Phasellus faucibus ut purus a condimentum. Sed id risus eget sem Phasellus faucibus ut condim tumsodalesm quis.</p>
  </div>
  <div class="abs obit" style="left:788px;top:126px">
    <div class="photo" role="img" aria-label="Black and white portrait photograph"></div>
    <div class="meta"><b class="name">Victor Hale</b><span class="role">Amazing Man</span><br><b>From:</b> 11.08.1937<br><b>To:</b> 14.03.2015</div>
    <p class="desc">Phasellus faucibus ut purus a condimentum. Sed id risus eget sem Phasellus faucibus ut condim tumsodalesm quis.</p>
  </div>
  <span class="btn" style="left:515px;top:353px;width:168px;height:41px">View All Obituries</span>
</section>

<h2 class="section-title" style="top:1630px">Our Shop</h2>
<p class="abs" style="left:380px;top:1683px;width:440px;text-align:center;font-size:12px;line-height:15px">Etiam sit amet orci eget eros faucibus tincidunt. Duis leo. Sed fringilla mauris sit amet nibh.</p>
<div class="abs product" style="left:138px;top:1764px">
  <div class="pic" role="img" aria-label="Bouquet of yellow tulips" style="background:radial-gradient(ellipse at 50% 35%,#f6d21c 0%,#e8b80c 45%,#6f9a2a 70%,#fff 72%)"></div>
  <div class="name">Beautiful In Blue</div><div class="price">$ 44.00</div>
</div>
<div class="abs product" style="left:376px;top:1764px">
  <div class="pic" role="img" aria-label="Two white pillar candles" style="background:radial-gradient(ellipse at 50% 55%,#f4ece2 0%,#e2d6c8 40%,#fff 62%)"></div>
  <div class="name" style="margin-top:37px">White Candles</div><div class="price" style="margin-top:6px">$ 30.00</div>
</div>
<div class="abs product" style="left:616px;top:1764px">
  <div class="pic" role="img" aria-label="Bouquet of orange and red gerbera flowers" style="background:radial-gradient(ellipse at 50% 45%,#f7a21e 0%,#e94e1b 40%,#4e8a2c 62%,#fff 66%)"></div>
  <div class="name" style="margin-top:44px">Peaceful Orange</div><div class="price" style="margin-top:6px">$ 51.00</div>
</div>
<div class="abs product" style="left:866px;top:1764px">
  <div class="pic" role="img" aria-label="Two white candles on a stand" style="background:radial-gradient(ellipse at 50% 55%,#f1f1f1 0%,#dcdcdc 35%,#fff 55%)"></div>
  <div class="name" style="margin-top:44px">Candles with stand</div><div class="price" style="margin-top:6px">$ 21.00</div>
</div>
<span class="btn" style="left:154px;top:2078px;width:168px;height:40px">Purchase</span>
<span class="btn" style="left:396px;top:2078px;width:168px;height:40px">Purchase</span>
<span class="btn" style="left:637px;top:2078px;width:168px;height:40px">Purchase</span>
<span class="btn" style="left:878px;top:2078px;width:168px;height:40px">Purchase</span>

<section class="abs monument" role="img" aria-label="Lit candle beside white roses in soft focus">
  <h2>Funeral Monument</h2>
  <div class="copy">
    <p>Lorem ipsum dolor sit amet, consectetur adipisicing do eiusmod tempor incididunt ut labore et dolore magna aliqua. Ut enim ad minim veniam, quis nostrud Lorem ipsum dolor sit amet, consectetur adipisicing do eiusmod tempor incididunt ut labore et dolore magna aliqua. Ut enim ad minim veniam, quis nostrud Lorem ipsum dolor sit amet, consectetur adipisicing do eiusmod tempor incididunt ut labore et dolore magna aliqua. Ut enim ad minim veniam, quis nostrud.</p>
    <p>Lorem ipsum dolor sit amet, consectetur adipisicing do eiusmod tempor incididunt ut labore et dolore magna aliqua. Ut enim ad minim veniam, quis nostrud Lorem ipsum dolor sit amet, consectetur adipisicing do eiusmod tempor incididunt ut labore et dolore magna aliqua. Ut enim ad minim veniam, quis nostrud Lorem ipsum dolor sit amet, consectetur adipisicing do eiusmod tempor incididunt ut labore et dolore magna aliqua.</p>
    <p>Ut enim ad minim veniam, quis nostrud Lorem ipsum dolor sit amet, consectetur adipisicing do eiusmod tempor incididunt ut labore et dolore magna aliqua. Ut enim ad minim veniam.</p>
  </div>
  <div class="dots" style="left:586px;top:352px"><i></i><i></i><i></i></div>
</section>

<div class="abs contact" style="left:132px;top:2672px;width:478px">
  <h2>Contact Us</h2>
  <p class="lead" style="margin-top:18px">Lorem ipsum dolor sit amet, consectetuer adipiscing elit. Aenean commodo ligula eget dolor. Aenean massa. Cum sociis natoque penatibus et magnis dis parturient montes, nascetur ridiculus mus. Donec quam felis, ultricies nec, pellentesque eu, pretium quis, sem.</p>
</div>
<div class="abs info-item" style="left:132px;top:2824px">
  <span class="ic"><svg width="14" height="19" viewBox="0 0 9 12"><path d="M4.5 0A4.5 4.5 0 0 0 0 4.5C0 8 4.5 12 4.5 12S9 8 9 4.5A4.5 4.5 0 0 0 4.5 0zm0 6.2a1.7 1.7 0 1 1 0-3.4 1.7 1.7 0 0 1 0 3.4z" fill="#fff"/></svg></span>
  <div><h3>ADDRESS</h3><p>48, Willow Lane,<br>Cedar Street<br>Fl, United States</p></div>
</div>
<div class="abs info-item" style="left:394px;top:2824px">
  <span class="ic"><svg width="22" height="22" viewBox="0 0 22 22"><circle cx="11" cy="11" r="9" fill="none" stroke="#fff" stroke-width="2.2"/><path d="M11 5v6h5" stroke="#fff" stroke-width="2.2" fill="none"/></svg></span>
  <div><h3>OPENING HOURS</h3><p>Monday to Friday: 9am to 7pm<br>Saturday: 9am to 4pm<br>Sunday: 11am to 4pm</p></div>
</div>
<div class="abs info-item" style="left:132px;top:2951px">
  <span class="ic"><svg width="20" height="14" viewBox="0 0 20 14"><rect x="1" y="1" width="18" height="12" fill="none" stroke="#fff" stroke-width="2"/><path d="M1 1l9 7 9-7" fill="none" stroke="#fff" stroke-width="2"/></svg></span>
  <div><h3>EMAIL</h3><p>support@evermorehome.example<br>service@evermorehome.example</p></div>
</div>
<div class="abs info-item" style="left:394px;top:2951px">
  <span class="ic"><svg width="18" height="18" viewBox="0 0 24 24"><path d="M6.6 10.8a15 15 0 0 0 6.6 6.6l2.2-2.2c.3-.3.7-.4 1-.2 1.1.4 2.3.6 3.6.6.6 0 1 .4 1 1V20c0 .6-.4 1-1 1A17 17 0 0 1 3 4c0-.6.4-1 1-1h3.5c.6 0 1 .4 1 1 0 1.3.2 2.5.6 3.6.1.3 0 .7-.2 1z" fill="#fff"/></svg></span>
  <div><h3>PHONE</h3><p>Call customer service on<br>1800-5550-4412</p></div>
</div>
<div class="abs" style="left:233px;top:3063px;width:276px;height:1px;background:#ddd"></div>
<div class="abs contract" style="left:134px;top:3098px;width:476px">
  <h2>Funeral Contract</h2>
  <p class="lead" style="margin-top:18px">Lorem ipsum dolor sit amet, consectetuer adipiscing elit. Aenean commodo ligula eget dolor.</p>
</div>
<span class="btn" style="left:132px;top:3199px;width:253px;height:41px">Download Contract Form</span>

<div class="abs form">
  <h2>Drop us a line</h2>
  <label>Your Name (Required)</label><div class="field"></div>
  <label>Your Email (Required)</label><div class="field"></div>
  <label>Your Phone Number</label><div class="field"></div>
  <label>Your Message</label><div class="field tall"></div>
  <span class="btn" style="left:95px;top:543px;width:168px;height:41px">Send Message</span>
</div>

<footer class="abs footer">
  <h3 style="left:134px">About us</h3>
  <p class="txt" style="left:132px;width:328px">Lorem ipsum dolor sit amet, consectetuer adipiscing elit. Aenean commodo ligula eget dolor. Aenean massa. Cum sociis natoque penatibus et magnis dis parturient montes, nascetur ridiculus mus. Donec quam felis, ultricies nec, pellentesque eu, pretium quis, sem.</p>
  <h3 style="left:506px">Services We Offer</h3>
  <div class="links" style="left:504px">
    <span>Arranging Funeral</span><span>Arrangement of flowers</span>
    <span>Memorials</span><span>Life Art Coffin</span>
    <span>Legal Services</span><span>Arranging Limousine</span>
    <span>Burial &amp; Cremation</span><span>Arrangement of priest</span>
  </div>
  <h3 style="left:831px">Testimonials</h3>
  <span class="abs" style="left:806px;top:86px;font-family:var(--serif);font-size:48px;color:rgba(255,255,255,.25)">&ldquo;</span>
  <p class="txt" style="left:827px;width:240px;top:103px">I wanted to take a moment and thank you again for the very nice service you performed for Ellen's memorial. I had several people come up to me to say "what a wonderful funeral". It was a nice tribute to him." &nbsp;&nbsp;- Thomas Reed</p>
</footer>
<div class="abs bottom">
  <div class="abs legal"><span>© 2019 All Rights Reserved</span><span>Terms &amp; Conditions</span><span>Privacy Policies</span></div>
  <div class="abs social"><span>Social Media Links</span><i></i><i></i><i></i><i></i></div>
</div>

</body>
</html>
```